Tideward Fuel Product design

We need a bottle design for our product. Tideward Fuel is a Gaming Nootropic made to increase Energy, Focus, Reaction time, and Clarity of an eSport gamer. It will be 40 servings a bottle. Currently, all the ingredients haven't been finalized so after the competition is over we will have to work with the designer to also make an ingredients label for the back of it. For the flavor, we will call it ember dusk.

The attachments included:. The velvet mongoose picture as a font style I like for the logo.
The K BOLT SURGEWAVE PICTURE IS WHAT WE WANT OUR DESIGN to look like something similar a clean and simple design that stands out!

K Bolt bottle is what our biggest competitors product looks like. The tideward fuel picture as the current logo we are using but can be changed.

Overall the pictures are just some references for what I could possibly want the design to look like however, I'm open to your designer's ideas and concepts you think would make for a cool looking Gaming Nootropic product bottle design. I appreciate everyone working on this and look forward to seeing your designs have a great day!

Target Market(s)

Gamers between the ages of 18-30

Industry/Entity Type

Health And Wellness

Requirements
Must have
• Tideward Fuel logo, state that it is for energy, focus, reaction, and clarity. state 40 serivngs. state flavor.

```html
<!DOCTYPE html>
<html lang="en">
<head>
<meta charset="utf-8">
<title>Tideward Fuel – Tub Label</title>
<link rel="stylesheet" href="https://fonts.googleapis.com/css2?family=Archivo+Black&family=Kanit:wght@600&family=Arimo:wght@400;700&display=swap">
<style>
  :root {
    --page: #ffffff;
    --tub: #eaeceb;
    --tub-line: #5a5a5a;
    --label-cyan: #43d8e6;
    --claim-red: #e11f26;
    --claim-yellow: #fff200;
    --flavor-blue: #05a0df;
    --art-top: #3fc3ec;
    --art-bottom: #2aa8e4;
    --brand-ink: #262626;
    --badge-fill: #2d9fe0;
    --badge-ring: #1d3f9b;
    --white: #ffffff;
  }
  html, body {
    margin: 0;
    padding: 0;
    width: 1200px;
    height: 1054px;
    overflow: hidden;
    background: var(--page);
  }
  .tub-design {
    display: block;
    width: 1200px;
    height: 1054px;
  }
  .tub-lid, .tub-body { fill: var(--tub); stroke: var(--tub-line); stroke-width: 2; }
  .label-band { fill: var(--label-cyan); }
  .claim-strip { fill: var(--claim-red); }
  .claim-text {
    font-family: "Kanit", sans-serif;
    font-weight: 600;
    font-size: 44px;
    fill: var(--claim-yellow);
  }
  .brand-name {
    font-family: "Archivo Black", sans-serif;
    font-size: 116px;
    fill: var(--brand-ink);
  }
  .flavor-band { fill: var(--flavor-blue); stroke: var(--white); stroke-width: 2; }
  .flavor-text {
    font-family: "Arimo", sans-serif;
    font-size: 58px;
    fill: var(--white);
  }
  .servings-badge { fill: var(--badge-fill); stroke: var(--badge-ring); stroke-width: 2; }
  .servings-text {
    font-family: "Arimo", sans-serif;
    font-weight: 700;
    font-size: 56px;
    fill: var(--white);
    stroke: var(--brand-ink);
    stroke-width: 2;
    paint-order: stroke;
  }
</style>
</head>
<body>
<svg class="tub-design" viewBox="0 0 1200 1054" xmlns="http://www.w3.org/2000/svg">
  <defs>
    <linearGradient id="art-gradient" x1="0" y1="0" x2="0" y2="1">
      <stop offset="0" stop-color="var(--art-top)"/>
      <stop offset="1" stop-color="var(--art-bottom)"/>
    </linearGradient>
  </defs>

  <path class="tub-lid" d="M104 112 Q104 102 116 102 L1064 102 Q1076 102 1076 114 L1076 218 L1048 228 L1054 236 L104 236 L108 228 L104 218 Z"/>

  <path class="tub-body" d="M150 236 L1040 236 Q1086 248 1088 280 L1088 896 Q1088 936 1046 939 L150 939 Q100 936 98 896 L98 280 Q102 248 150 236 Z"/>

  <rect class="label-band" x="97" y="269" width="988" height="580"/>

  <rect role="img" aria-label="Illustration area: ice glacier artwork" fill="url(#art-gradient)"
        x="480" y="356" width="605" height="493"/>

  <rect class="claim-strip" x="97" y="290" width="988" height="66"/>
  <text class="claim-text" x="148" y="340" textLength="910" lengthAdjust="spacing">ENERGY&#160;&#160;|&#160;&#160;FOCUS&#160;&#160;|&#160;&#160;REACTION&#160;&#160;|&#160;&#160;CLARITY</text>

  <text class="brand-name" x="195" y="501" textLength="623" lengthAdjust="spacingAndGlyphs">TIDEWARD</text>
  <text class="brand-name" x="665" y="630" text-anchor="middle">FUEL</text>

  <path class="flavor-band" d="M97 702 L480 702 L508 757 L1085 757 L1085 828 L97 828 Z"/>
  <text class="flavor-text" x="128" y="789">ember dusk</text>

  <circle class="servings-badge" cx="999" cy="693" r="55"/>
  <text class="servings-text" x="999" y="713" text-anchor="middle">40</text>
</svg>
</body>
</html>
```